Clean and modern business cards

Looking for an updated business card design for my dental office “corvanta dental” . Looking for a modern clean / sleek design . I’m thinking black background but open to seeing other options . One side needs to have an appointment card . Card needs to have logo, dentist name , phone, email , address . I’ve attached couple of cards I thought were cool as well as my logo
Target Market(s)
Dental patients
Industry/Entity Type
Dentistry
Contact Information for Business Card
Phone email address

```html
<!DOCTYPE html>
<html lang="en">
<head>
<meta charset="utf-8">
<title>Corvanta Dental – Business Card</title>
<link href="https://fonts.googleapis.com/css2?family=Open+Sans:wght@400;600;700;800&display=swap" rel="stylesheet">
<style>
  :root {
    --bg: #8a8b8f;
    --card: #050505;
    --edge: #1f8fb0;
    --white: #ffffff;
    --teal: #1aa3c4;
    --purple: #6a2aa0;
    --lime: #9cc21e;
    --yellow: #f3c31a;
    --red: #e8321c;
    --panel-a: #16222a;
    --panel-b: #1c1426;
  }
  * { box-sizing: border-box; margin: 0; padding: 0; }
  html, body { width: 1200px; height: 1050px; overflow: hidden; }
  body {
    background: linear-gradient(160deg, #7b7c80, var(--bg));
    font-family: "Open Sans", Arial, sans-serif;
    color: var(--white);
    position: relative;
  }
  .card {
    position: absolute;
    left: 250px;
    width: 700px;
    height: 400px;
    background: var(--card);
    border-bottom: 4px solid var(--edge);
    border-right: 4px solid var(--edge);
    overflow: hidden;
    box-shadow: 0 18px 40px rgba(0,0,0,.35);
  }
  .card--back { top: 80px; }
  .card--front { top: 565px; }

  /* back side */
  .back-brand {
    position: absolute;
    inset: 0;
    display: flex;
    align-items: center;
    justify-content: center;
    gap: 16px;
  }
  .brand-dot {
    width: 30px; height: 30px; border-radius: 50%;
    background: var(--teal);
    flex: none;
  }
  .back-brand .brand-name {
    font-size: 34px;
    font-weight: 700;
    letter-spacing: 2px;
    text-transform: uppercase;
  }

  /* front side */
  .front-brand {
    position: absolute;
    left: 46px; top: 42px;
    display: flex; align-items: center; gap: 14px;
  }
  .front-brand .brand-dot { width: 60px; height: 60px; }
  .front-brand .brand-name {
    font-size: 28px;
    font-weight: 700;
    letter-spacing: 1px;
    text-transform: uppercase;
    line-height: 1;
  }

  .appointment-panel {
    position: absolute;
    left: 24px; top: 128px;
    width: 320px; height: 240px;
    border-radius: 18px;
    background: linear-gradient(135deg, var(--panel-a), var(--panel-b));
  }
  .appointment {
    position: absolute;
    left: 48px; top: 176px;
    width: 272px;
  }
  .appointment-title {
    font-size: 16px; font-weight: 700;
    text-align: center;
    margin-bottom: 24px;
  }
  .field {
    display: flex; align-items: center; gap: 8px;
    font-size: 14px;
    margin-bottom: 24px;
  }
  .field-line {
    flex: 1; height: 14px; border-radius: 7px;
    background: var(--white);
  }

  .contact {
    position: absolute;
    left: 520px; top: 215px;
    width: 330px; height: 250px;
    transform: translate(-50%, -50%) rotate(-90deg);
    padding: 10px 0 0 10px;
  }
  .contact-name {
    font-size: 22px; font-weight: 700;
    text-transform: uppercase; letter-spacing: .5px;
    line-height: 1.1;
  }
  .contact-role { font-size: 14px; margin-bottom: 12px; }
  .contact-group {
    border-top: 1px solid var(--purple);
    padding: 8px 0 10px;
    font-size: 14px; line-height: 1.35;
  }
  .contact-group--reach { border-top-color: var(--lime); }
  .contact-row { display: flex; align-items: center; gap: 8px; letter-spacing: .5px; }
  .contact-row svg { width: 12px; height: 12px; flex: none; }
  .contact-row .phone-num { letter-spacing: 3px; }
</style>
</head>
<body>

  <section class="card card--back" aria-label="Card back">
    <div class="back-brand">
      <span class="brand-dot"></span>
      <span class="brand-name">Corvanta Dental</span>
    </div>
  </section>

  <section class="card card--front" aria-label="Card front">
    <div class="front-brand">
      <span class="brand-dot"></span>
      <span class="brand-name">Corvanta Dental</span>
    </div>

    <div class="appointment-panel" role="img" aria-label="Decorative area behind the appointment details"></div>

    <div class="appointment">
      <p class="appointment-title">Your Next Appointment</p>
      <div class="field"><span>Time:</span><span class="field-line"></span></div>
      <div class="field"><span>Date:</span><span class="field-line"></span></div>
    </div>

    <div class="contact">
      <p class="contact-name">Dr. Elias Varrenko</p>
      <p class="contact-role">Director</p>
      <div class="contact-group">
        <p>2840 Marlowe Ave,</p>
        <p>Winnipeg, MB</p>
      </div>
      <div class="contact-group contact-group--reach">
        <p class="contact-row">
          <svg viewBox="0 0 12 12"><path d="M2 1l2 0 1 3-1.5 1a6 6 0 0 0 3.5 3.5L8 7l3 1v2a1 1 0 0 1-1 1A9 9 0 0 1 1 2a1 1 0 0 1 1-1z" fill="var(--red)"/></svg>
          <span class="phone-num">204-555-0187</span>
        </p>
        <p class="contact-row">
          <svg viewBox="0 0 12 12"><rect x="1" y="2.5" width="10" height="7" fill="var(--yellow)"/><path d="M1 2.5l5 4 5-4" fill="none" stroke="#050505" stroke-width="1"/></svg>
          <span>contact@corvantawpg.ca</span>
        </p>
        <p class="contact-row">
          <svg viewBox="0 0 12 12"><circle cx="6" cy="6" r="5" fill="none" stroke="var(--teal)" stroke-width="1.3"/><path d="M1 6h10M6 1v10M3 3.5h6M3 8.5h6" stroke="var(--teal)" stroke-width=".8"/></svg>
          <span>www.corvantawpg.ca</span>
        </p>
      </div>
    </div>
  </section>

</body>
</html>
```